Business card for law firm

Need business card for new law firm. Think confident, authoritative, conservative, but not stuffy or old-fashioned.

Contact Information for Business Card

Content for card - logo (uploaded), plus the following:

Paul Wexbury (larger font)
Managing Partner (larger font, but not as large as name)
Level 9, 41 Tansy Lane
Sydney NSW 2000
Main Tel 02 7346 2190
Direct Tel 02 6273 4415
Email paul@qvlegal.com.au
www.qvlegal.com.au

Letterhead design should include logo plus:
Level 9, 41 Tansy Lane
Sydney NSW 2000
Tel 02 6273 4415
www.qvlegal.com.au

```html
<!DOCTYPE html>
<html lang="en">
<head>
<meta charset="utf-8">
<title>Quayvale Lawyers – Business Card</title>
<link href="https://fonts.googleapis.com/css2?family=Jost:wght@400;500;700&display=swap" rel="stylesheet">
<style>
  :root {
    --navy: #0d2163;
    --navy-deep: #0a1a52;
    --ink: #111111;
    --paper: #ffffff;
    --backdrop: #3a3a3c;
  }
  * { margin: 0; padding: 0; box-sizing: border-box; }
  html, body {
    width: 1200px; height: 1000px; overflow: hidden;
    background: var(--backdrop);
    font-family: "Jost", sans-serif;
  }
  .card {
    position: absolute;
    left: 290px;
    width: 620px; height: 380px;
    border-radius: 26px;
    overflow: hidden;
  }
  .card-back { top: 50px; background: var(--navy); color: var(--paper); }
  .card-front { top: 570px; background: var(--paper); }

  .brand { position: absolute; text-align: center; font-weight: 400; }
  .brand-mark { display: block; margin: 0 auto 10px; width: 58px; height: 58px; }
  .brand-name { display: block; font-size: 50px; letter-spacing: 2px; line-height: 1; }
  .brand-sub { display: block; font-size: 17px; letter-spacing: 15px; margin-top: 4px; padding-left: 15px; }

  .card-back .brand { left: 0; right: 0; top: 78px; color: var(--paper); }
  .card-back .brand-mark { background: var(--paper); }
  .back-web {
    position: absolute; left: 0; right: 0; top: 292px;
    text-align: center; font-size: 17px; letter-spacing: 0.5px;
  }

  .card-front .brand { left: 40px; top: 34px; width: 330px; color: var(--ink); }
  .card-front .brand-mark { background: var(--navy); }
  .card-front .brand-name { font-size: 46px; }
  .card-front .brand-sub { font-size: 16px; letter-spacing: 14px; }

  .wave { position: absolute; left: 0; top: 0; width: 620px; height: 380px; }

  .person { position: absolute; right: 34px; top: 92px; text-align: right; }
  .person-name { color: var(--navy); font-weight: 700; font-size: 21px; letter-spacing: 0.5px; text-transform: uppercase; }
  .person-role { color: var(--ink); font-size: 18px; margin-top: 1px; }

  .address { position: absolute; right: 34px; top: 196px; text-align: right; color: var(--ink); font-size: 15.5px; line-height: 1.35; }

  .contacts { position: absolute; right: 34px; top: 282px; text-align: right; color: var(--paper); font-size: 15px; line-height: 1.4; }
  .contacts b { font-weight: 700; }
  .contacts .row { display: flex; justify-content: flex-end; align-items: center; gap: 7px; }
  .contacts svg { width: 13px; height: 13px; }
</style>
</head>
<body>

<section class="card card-back" aria-label="Card back">
  <div class="brand">
    <span class="brand-mark"></span>
    <span class="brand-name">QUAYVALE</span>
    <span class="brand-sub">LAWYERS</span>
  </div>
  <div class="back-web">www.qvlegal.com.au</div>
</section>

<section class="card card-front" aria-label="Card front">
  <svg class="wave" viewBox="0 0 620 380" aria-hidden="true">
    <path fill="var(--ink)" d="M0,128 C100,225 250,272 405,268 C250,258 110,214 0,148 Z"/>
    <path fill="var(--navy)" d="M0,172 C110,248 260,284 405,270 C490,262 560,246 620,238 L620,380 L0,380 Z"/>
  </svg>

  <div class="brand">
    <span class="brand-mark"></span>
    <span class="brand-name">QUAYVALE</span>
    <span class="brand-sub">LAWYERS</span>
  </div>

  <div class="person">
    <div class="person-name">Paul Wexbury</div>
    <div class="person-role">Managing Partner</div>
  </div>

  <div class="address">
    Level 9, 41 Tansy Lane<br>
    Sydney NSW 2000
  </div>

  <div class="contacts">
    <div class="row"><span><b>Main Tel</b> 02 7346 2190</span></div>
    <div class="row"><span><b>Direct Tel</b> 02 6273 4415</span></div>
    <div class="row"><span>paul@qvlegal.com.au</span>
      <svg viewBox="0 0 14 14" aria-hidden="true"><rect x="1" y="3" width="12" height="8" fill="none" stroke="#fff" stroke-width="1.3"/><path d="M1,3 L7,8 L13,3" fill="none" stroke="#fff" stroke-width="1.3"/></svg>
    </div>
    <div class="row"><span>www.<b>qvlegal</b>.com.au</span>
      <svg viewBox="0 0 14 14" aria-hidden="true"><circle cx="7" cy="7" r="5.8" fill="none" stroke="#fff" stroke-width="1.2"/><ellipse cx="7" cy="7" rx="2.5" ry="5.8" fill="none" stroke="#fff" stroke-width="1"/><path d="M1.2,7 H12.8" stroke="#fff" stroke-width="1"/></svg>
    </div>
  </div>
</section>

</body>
</html>
```